Vortane Labs - Methylene Blue Product Packaging

Our brand is Vortane Labs. We are launching a new product that is Methylene Blue, you can see more about this product if you search on Brisko or Pelludo and you will see what it is. This will be for a 50ml bottle. Give me different options for packaging that is minimalist and clean for this brand that makes it look well made and make people want to buy. I've added examples of what the bottle shape will be and potential packaging shapes so you can make packaging on those based off of that.

```html
<!DOCTYPE html>
<html lang="en">
<head>
<meta charset="UTF-8">
<title>Vortane Labs – Methylene Blue 50ml Label</title>
<link rel="stylesheet" href="https://fonts.googleapis.com/css2?family=Bebas+Neue&family=Montserrat:wght@600&family=Poppins:wght@600&family=Raleway:wght@500&display=swap">
<style>
  :root {
    --page-bg: #ffffff;
    --label-bg: #2d2d2d;
    --label-bg-light: #3a3a3a;
    --brand-grey: #cfcfcf;
    --title-grey: #d6d6d6;
    --accent-blue: #2a9fe6;
    --pill-text: #1f2a33;
    --body-text: #cbcbcb;
    --pattern-tone: rgba(42, 120, 180, 0.10);
  }
  * { margin: 0; padding: 0; box-sizing: border-box; }
  html, body {
    width: 1200px;
    height: 1200px;
    overflow: hidden;
    background: var(--page-bg);
  }
  .canvas {
    position: relative;
    width: 1200px;
    height: 1200px;
  }
  .label {
    position: absolute;
    left: 300px;
    top: 190px;
    width: 600px;
    height: 820px;
    border-radius: 28px;
    background: linear-gradient(90deg, var(--label-bg) 0%, var(--label-bg-light) 50%, var(--label-bg) 100%);
    overflow: hidden;
  }
  .label__pattern {
    position: absolute;
    left: 0;
    right: 0;
    top: 250px;
    bottom: 0;
    background: linear-gradient(180deg, rgba(42,120,180,0) 0%, var(--pattern-tone) 30%, var(--pattern-tone) 100%);
  }
  .brand {
    position: absolute;
    left: 70px;
    top: 70px;
    width: 460px;
    text-align: right;
    font-family: "Montserrat", sans-serif;
    font-weight: 600;
    color: var(--brand-grey);
  }
  .brand__name {
    display: block;
    font-size: 84px;
    line-height: 0.95;
    letter-spacing: -2px;
  }
  .brand__sub {
    display: block;
    font-size: 60px;
    line-height: 1;
    letter-spacing: -1px;
  }
  .product {
    position: absolute;
    left: 0;
    width: 100%;
    text-align: center;
    font-family: "Bebas Neue", sans-serif;
  }
  .product__kind {
    top: 318px;
    font-size: 86px;
    line-height: 1;
    color: var(--title-grey);
    letter-spacing: -1px;
  }
  .product__name {
    top: 388px;
    font-size: 200px;
    line-height: 1;
    color: var(--accent-blue);
    letter-spacing: -2px;
  }
  .volume {
    position: absolute;
    left: 197px;
    top: 596px;
    width: 206px;
    height: 56px;
    border-radius: 28px;
    background: var(--accent-blue);
    color: var(--pill-text);
    font-family: "Poppins", sans-serif;
    font-weight: 600;
    font-size: 32px;
    line-height: 56px;
    text-align: center;
  }
  .certified {
    position: absolute;
    left: 0;
    top: 690px;
    width: 100%;
    text-align: center;
    font-family: "Raleway", sans-serif;
    font-weight: 500;
    color: var(--body-text);
  }
  .certified__figure {
    display: block;
    font-family: "Poppins", sans-serif;
    font-weight: 600;
    font-size: 36px;
    line-height: 1.2;
  }
  .certified__text {
    display: block;
    font-size: 40px;
    line-height: 1.5;
  }
</style>
</head>
<body>
  <main class="canvas">
    <section class="label">
      <div class="label__pattern" role="img" aria-label="Faint blue hexagon molecule pattern across the lower label"></div>

      <div class="brand">
        <span class="brand__name">Vortane</span>
        <span class="brand__sub">Labs</span>
      </div>

      <h1 class="product product__kind">Methylene</h1>
      <p class="product product__name">Blue</p>

      <div class="volume">50ml</div>

      <p class="certified">
        <span class="certified__figure">100%</span>
        <span class="certified__text">Lab Certified</span>
      </p>
    </section>
  </main>
</body>
</html>
```